Postcard Design

I have prduced a documentary film and I would like to create a post card to help promote and announce the film and how to purchase the film. my web site shold be mentioned KelmorProductions.com

There is a discription of the current FILM called DORIAN at the above web site .

I think I wil also use DORIAN the movie .com as a registered do mane name

The flip side of the card should promote a conference, that is still being planned, but information can be found at Ashgrove summit.com the event will be in Heber in 2015 November 5 -6-7, 2015. It will be the 40th anniversary of this historic UFO encounter which my documentary is focused.

Meet Dorian Pelk and other UFO experts at this three day conference.

Visit the acutual encounter location in the Colburne National Forrest with Dorian Thursday November 5th, 2015. 40 years to the date of his dissapearence. Night watch lead by Carl Mireau and Dorian Pelk.

The second site of the post card promoting the film annoucment should promote the upcoming Dorian Pelk 40th Aniversary UFO conference on NOvember 5th 2015 to November 8th. In Heber Arizona. visit: http://www.ashgrovesummit.com for more information. You can pull some information form the site. I have also uploaded graphics for this announcement. I like the first design posted but the wording should be improved to read better... there is wording on the dvd cover to draw from that is better langueged. It was a UFO incident or "encounter" of the third kind, is even a better description. It made international headlines and contiues to to astound UFO researchers, journalist, police, and the media. rather than just a UFO event.

Target Market(s)

This market will be people interested in comming to a UFO conference, or interested in learning about this topic thru film. Can be all walks of people form al different socio economic backgrounds. There are the people hunger for information that has been hidden from them, other experiencers especially like to meet people of a like mind where they can speak freely with out fear of ridicule.

Industry/Entity Type

Movie

Font styles to use
Serif

Colors
faa54b
9d9d9d
fece3f

Requirements
Must have
• Current web sites on one card are wrong,

Movie web site is DorianPelkthemovie.com

Web site for conference is www.ashgrovesummit.com

Web sites listed, as this shows how to buy the film and how to register for the conference. For the film side of the card it should say for screening inquires contact Marla K. Dupree - Kelmor Productions.com
Nice to have
• Idealy I'd like to have a promo card that is two sided with out being a mailer. Can this be done?

You can take grphics form the ash grove summit web site too if you want for the promo card siade about the conference.

```html
<!DOCTYPE html>
<html lang="en">
<head>
<meta charset="utf-8">
<title>DORIAN – Conference Postcard</title>
<link rel="stylesheet" href="https://fonts.googleapis.com/css2?family=Bowlby+One&family=Crimson+Text&display=swap">
<style>
  :root {
    --page-bg: #e4ddd3;
    --card-dark: #141010;
    --forest-glow: #faa54b;
    --forest-ember: #c8701e;
    --forest-shadow: #2a1a10;
    --night-grey: #3b3b3b;
    --night-deep: #262626;
    --title-yellow: #fece3f;
    --text-white: #ffffff;
    --stamp-line: #000000;
    --address-line: #000000;
  }
  * { margin: 0; padding: 0; box-sizing: border-box; }
  html, body {
    width: 1200px;
    height: 817px;
    overflow: hidden;
    background: var(--page-bg);
  }
  .postcard {
    position: absolute;
    left: 205px;
    top: 75px;
    width: 820px;
    height: 632px;
    background: var(--card-dark);
    overflow: hidden;
  }
  .forest-photo {
    position: absolute;
    left: 0;
    top: 0;
    width: 413px;
    height: 632px;
    background:
      radial-gradient(ellipse 90px 220px at 50px 390px, var(--forest-glow) 0%, var(--forest-ember) 40%, rgba(120,60,20,0.5) 75%, transparent 100%),
      radial-gradient(ellipse 260px 260px at 150px 470px, rgba(160,80,25,0.55) 0%, transparent 80%),
      linear-gradient(180deg, #0c0908 0%, var(--forest-shadow) 60%, #120b07 100%);
  }
  .night-illustration {
    position: absolute;
    left: 413px;
    top: 0;
    width: 407px;
    height: 632px;
    background: linear-gradient(180deg, var(--night-deep) 0%, var(--night-grey) 55%, #4a4a48 100%);
  }
  .film-title {
    position: absolute;
    left: 19px;
    top: 28px;
    font-family: "Bowlby One", serif;
    font-size: 36px;
    line-height: 1;
    letter-spacing: 1px;
    color: var(--title-yellow);
  }
  .tagline {
    position: absolute;
    left: 19px;
    top: 74px;
    font-family: "Crimson Text", serif;
    font-size: 33px;
    line-height: 37px;
    color: var(--text-white);
  }
  .event-details {
    position: absolute;
    left: 146px;
    top: 232px;
    width: 265px;
    font-family: "Crimson Text", serif;
    font-size: 25px;
    line-height: 30px;
    color: var(--text-white);
  }
  .drop-cap {
    float: left;
    font-size: 68px;
    line-height: 52px;
    margin: 4px 4px 0 0;
  }
  .event-site {
    font-size: 22px;
  }
  .screening-contact {
    position: absolute;
    left: 19px;
    top: 468px;
    font-family: "Crimson Text", serif;
    font-size: 24px;
    line-height: 30px;
    color: var(--text-white);
  }
  .stamp-box {
    position: absolute;
    left: 688px;
    top: 21px;
    width: 112px;
    height: 112px;
    background: #ffffff;
    border: 2px solid var(--stamp-line);
  }
  .address-lines {
    position: absolute;
    left: 0;
    top: 0;
  }
</style>
</head>
<body>
  <section class="postcard">
    <div class="forest-photo" role="img" aria-label="Photograph of a dark pine forest at night with glowing orange light between the trees"></div>
    <div class="night-illustration" role="img" aria-label="Painted illustration of an old pickup truck driving through a dark forest at night with headlights on"></div>

    <h1 class="film-title">DORIAN</h1>
    <p class="tagline">UFO encounter<br>of the third kind</p>

    <p class="event-details"><span class="drop-cap">D</span>orian Pelk<br>40th Anniversary<br>UFO conference from<br>November 5th to 8th,<br>2015 in Heber, Arizona.<br>Register online:<br><span class="event-site">www.ashgrovesummit.com</span></p>

    <p class="screening-contact">For screening inquiries<br>contact Marla K.<br>Dupree - Kelmor<br>Productions.com<br>DorianPelkthemovie.com</p>

    <div class="stamp-box" aria-label="Stamp area"></div>

    <svg class="address-lines" width="820" height="632" viewBox="0 0 820 632" aria-hidden="true">
      <g stroke="var(--address-line)" stroke-width="2">
        <line x1="512" y1="407" x2="801" y2="407"/>
        <line x1="468" y1="442" x2="801" y2="442"/>
        <line x1="468" y1="478" x2="801" y2="478"/>
        <line x1="468" y1="514" x2="801" y2="514"/>
        <line x1="468" y1="550" x2="801" y2="550"/>
      </g>
    </svg>
  </section>
</body>
</html>
```